Website redesign for Halt and reBloom

We would like to update the design of our current website to a more concise, conversion optimized design.
The goal of our website is to get our message across as concisely as possible plus encourage people to contact us for more information or to book a consultation.
We need a redesign of the home page and 1 internal page - just for design/layout purposes/format purposes.

Target Market(s)

Males 20-45 years old who are concerned about hair loss and who want to regrow their own hair.

Industry/Entity Type

Health And Wellness

Number of Pages Required

2 page

Font styles to use
Sans Serif

Colors
00a990
33a6d7
ffffff
9d9d9d

Requirements
Must have
• We want the home page to be very concise and to the point in getting the message across. We want to get across the following 6 key messages:
• 1. Dr Quimby story – why he created this solution
• 2. Hair loss is caused by a chemical imbalance
• 3. Halt and rebloom conducts genetic and DNA analysis, then rebalances body chemistry, thus reversing the hair loss process and enabling your own hair to regrow naturally
• 4. Money back guaranteed results
• 5. Only The Active ingredients – no harsh preservatives or chemicals are included
• 6. All ingredients are FDA approved and safe – no side effects
• We also need a strong call to action. We want people to call or email us to find out more information or to schedule a consultation.
• Here is our current website which is not performing as we would hope: http://www.haltandrebloom-example.com/
• Here is our press release for further information: https://www.pressdeskly-example.com/news/finally-we-now-have-a-cure-for-male-pattern-baldness-19187647
• I uploaded the logo files, but let me know if anything else is needed and I can add it.

```html
<!DOCTYPE html>
<html lang="en">
<head>
<meta charset="utf-8">
<title>Halt &amp; reBloom — Home</title>
<link rel="stylesheet" href="https://fonts.googleapis.com/css2?family=Montserrat:wght@400;500;600;700&family=Open+Sans:wght@400;600;700&display=swap">
<style>
:root{
  --green-dark:#0d4a3d;
  --green-band:#14574a;
  --footer:#1e3932;
  --blue:#1f9fd8;
  --ink:#1b1b1b;
  --body:#444;
  --grey:#9d9d9d;
  --white:#ffffff;
  --nav-dark:#1d1d1d;
  --gold:#d9a13a;
}
*{margin:0;padding:0;box-sizing:border-box}
html,body{width:1200px;height:2639px;overflow:hidden;background:var(--white)}
body{position:relative;font-family:"Open Sans",Arial,sans-serif;color:var(--body)}
.abs{position:absolute}
.topbar-left{left:0;top:0;width:580px;height:4px;background:var(--green-dark)}
.topbar-right{left:600px;top:0;width:600px;height:4px;background:var(--blue)}
.brand{left:96px;top:24px;display:flex;align-items:center;gap:14px}
.brand-mark{width:58px;height:58px;border-radius:50%;background:var(--green-dark)}
.brand-name{font-family:"Open Sans",Arial,sans-serif;font-size:32px;font-weight:400;color:var(--green-dark);line-height:1.15}
.brand-name small{display:block;font-size:22px}
.contact{top:38px;display:flex;gap:16px;align-items:flex-start;font-family:Georgia,serif;font-size:13px;color:#333;line-height:1.6}
.contact svg{flex:none}
.nav{left:90px;top:109px;width:1022px;height:51px;background:var(--green-dark);display:flex;z-index:2}
.nav a{color:var(--white);text-decoration:none;font-family:"Open Sans",Arial,sans-serif;font-size:16px;font-weight:600;line-height:51px;padding:0 16px;position:relative}
.nav a:first-child{margin-left:18px}
.nav a.active:after{content:"";position:absolute;left:16px;right:16px;bottom:12px;height:2px;background:var(--white)}
.nav .book{margin-left:auto;background:var(--nav-dark);padding:0 30px 0 26px;font-size:17px}
.hero{left:0;top:135px;width:1200px;height:472px;background:linear-gradient(90deg,#6e6158 0%,#b9a99c 30%,#dcd8d3 55%,#eeeeee 100%)}
.hero-copy{left:665px;top:270px;width:430px}
.hero-copy h1{font-family:"Montserrat",Arial,sans-serif;font-size:23px;font-weight:700;color:var(--ink);line-height:1.65}
.hero-copy p{font-size:13px;color:#333;line-height:1.6;margin-top:14px}
.btn-blue{display:inline-block;background:var(--blue);color:var(--white);font-family:"Montserrat",Arial,sans-serif;font-weight:600;font-size:15px;text-decoration:none;text-align:center}
.hero-copy .btn-blue{margin-top:22px;width:188px;height:46px;line-height:46px}
.intro-mark{left:576px;top:637px;width:48px;height:48px;border-radius:50%;background:var(--green-dark)}
.intro-title{left:0;top:718px;width:1200px;text-align:center;font-family:"Montserrat",Arial,sans-serif;font-variant:small-caps;font-size:29px;font-weight:500;color:var(--ink);letter-spacing:1px}
.intro-text{left:167px;top:768px;width:866px;text-align:center;font-size:12.5px;line-height:1.85;color:#333}
.card{top:910px;width:297px;height:208px;overflow:hidden}
.card .photo{width:100%;height:100%}
.card .caption{position:absolute;left:0;bottom:0;width:100%;height:51px;background:rgba(40,40,40,.78);color:var(--white);font-family:"Montserrat",Arial,sans-serif;font-weight:600;font-size:16px;line-height:51px;padding-left:22px}
.band{left:0;top:1225px;width:1200px;height:264px;background:linear-gradient(90deg,var(--green-band) 0%,#1a5f51 55%,#2d6a5e 80%,#1b5648 100%)}
.band-copy{left:0;top:1274px;width:1200px;text-align:center;color:var(--white)}
.band-copy .small{font-size:14px}
.band-copy .strong{font-family:"Montserrat",Arial,sans-serif;font-weight:600;font-size:17px;margin-top:12px}
.band-copy .btn-blue{margin-top:16px;width:463px;height:56px;line-height:56px;font-size:28px;font-weight:600}
.pitch{left:100px;top:1550px;width:1000px;text-align:center;font-family:"Montserrat",Arial,sans-serif;font-weight:600;font-size:19.5px;color:var(--ink);line-height:1.75}
.story{left:93px;top:1652px;width:510px;font-size:12.5px;line-height:1.84;color:#222}
.story p+p{margin-top:20px}
.video{left:620px;top:1660px;width:492px;height:299px;background:linear-gradient(135deg,#6a5446 0%,#b48a70 45%,#3a2c25 100%)}
.video-title{left:634px;top:1668px;font-size:14px;color:var(--white)}
.video-bar{left:620px;top:1945px;width:492px;height:14px;background:#000}
.footer{left:0;top:2001px;width:1200px;height:638px;background:var(--footer)}
.foot-mark{left:570px;top:2077px;width:60px;height:60px;border-radius:50%;background:#e6e6e6;opacity:.85}
.foot-tag{left:300px;top:2160px;width:600px;text-align:center;font-size:12.5px;line-height:1.9;color:#6f7f79}
.foot-rule{left:100px;width:1000px;height:1px;background:#34504a}
.socials{left:458px;top:2234px;display:flex;gap:14px}
.socials span{width:45px;height:45px;border-radius:50%;border:1px solid #4a615b}
.socials span.on{background:var(--blue);border-color:var(--blue)}
.col{top:2346px;color:var(--white)}
.col h3{font-family:"Montserrat",Arial,sans-serif;font-size:21px;font-weight:600;padding-bottom:14px;position:relative}
.col h3:after{content:"";position:absolute;left:0;bottom:0;width:60px;height:3px;background:var(--gold)}
.col h3:before{content:"";position:absolute;left:0;right:0;bottom:1px;height:1px;background:#3b554f}
.col p{font-size:12.5px;line-height:1.85;margin-top:14px}
.col-about{left:100px;width:296px}
.col-about p{color:#c9d1ce}
.col-hours{left:454px;width:236px}
.col-hours p{line-height:2.3;font-size:12.5px}
.col-address{left:764px;width:240px}
.addr{display:flex;gap:14px;margin-top:16px;font-size:12.5px;line-height:1.5}
.pin{width:30px;height:30px;border-radius:50%;background:var(--blue);flex:none;display:flex;align-items:center;justify-content:center}
.copyright{left:0;top:2604px;width:1200px;text-align:center;font-size:12.5px;color:#c9d1ce}
</style>
</head>
<body>
<div class="abs topbar-left"></div>
<div class="abs topbar-right"></div>

<header>
  <div class="abs brand">
    <span class="brand-mark"></span>
    <div class="brand-name">Halt &amp; reBloom<small>by Edwin Quimby M.D.</small></div>
  </div>
  <div class="abs contact" style="left:676px">
    <svg width="32" height="28" viewBox="0 0 32 28" aria-hidden="true"><path d="M4 10c0-5 6-7 12-7s12 2 12 7l-5 2-2-4H11l-2 4z" fill="none" stroke="#0d4a3d" stroke-width="2"/><rect x="8" y="13" width="16" height="12" rx="2" fill="none" stroke="#0d4a3d" stroke-width="2"/><circle cx="16" cy="19" r="3" fill="none" stroke="#0d4a3d" stroke-width="2"/></svg>
    <div>1-811-555-0142<br>1-811-555-0143</div>
  </div>
  <div class="abs contact" style="left:892px">
    <svg width="34" height="26" viewBox="0 0 34 26" aria-hidden="true"><rect x="1" y="2" width="32" height="22" fill="none" stroke="#0d4a3d" stroke-width="2"/><path d="M1 2l16 13L33 2" fill="none" stroke="#0d4a3d" stroke-width="2"/></svg>
    <div>info@examplemail.com<br>info@haltandrebloom-example.com</div>
  </div>
  <nav class="abs nav">
    <a href="#" class="active">Home</a>
    <a href="#">About Us</a>
    <a href="#">How it Works</a>
    <a href="#">Success Stories</a>
    <a href="#">Faq</a>
    <a href="#">Blog</a>
    <a href="#">Contact Us</a>
    <a href="#" class="book">Book an Appointment</a>
  </nav>
</header>

<section>
  <div class="abs hero" role="img" aria-label="Photo of a shirtless man checking his hairline in a bathroom mirror"></div>
  <div class="abs hero-copy">
    <h1>Stop Hereditary Hair Loss &amp; Regrow Full, Healthy Head of Hair</h1>
    <p>We offer various haircuts and beard trimming of all sorts. Our specialty is the trimming of your beard. You are in trusted hands with our stylists.</p>
    <a href="#" class="btn-blue">LEARN MORE</a>
  </div>
</section>

<section>
  <div class="abs intro-mark"></div>
  <h2 class="abs intro-title">Halt &amp; rebloom by Edwin Quimby M.D</h2>
  <p class="abs intro-text">Dr. Edwin Quimby, the creator of Halt and reBloom is a renowned hair restoration expert.&nbsp; After seeing first his father and then older brothers thin and go bald, he dedicated his life to finding the cure for hair loss. After initially pioneering the single hair method for hair transplant, he determined there must be a non-surgical solution and spent the last 20 years in research and clinical trial and error first creating.</p>
  <div class="abs card" style="left:125px">
    <div class="photo" role="img" aria-label="Photo of a man examining his receding hairline" style="background:linear-gradient(135deg,#d9d3cc,#a88c7a 60%,#6d5a4d)"></div>
    <div class="caption">Why Is Halt and reBloom Unique?</div>
  </div>
  <div class="abs card" style="left:449px">
    <div class="photo" role="img" aria-label="Photo of a man checking his hair in a hand mirror" style="background:linear-gradient(135deg,#e4e4ea,#b7aca6 55%,#5e4c44)"></div>
    <div class="caption">Personalized Medicine</div>
  </div>
  <div class="abs card" style="left:771px">
    <div class="photo" role="img" aria-label="Photo of a man touching his thinning hair" style="background:linear-gradient(135deg,#dad6d0,#b69c86 55%,#7a634f)"></div>
    <div class="caption">Holistic Approach</div>
  </div>
</section>

<section>
  <div class="abs band" role="img" aria-label="Green tinted photo of a man looking at his hairline"></div>
  <div class="abs band-copy">
    <p class="small">Sign Up For Our Newsletter - Receive Free Hair Regrowth Advice &amp; Special Offers</p>
    <p class="strong">The First Non-Surgical Hair Loss Solution With Clinically Proven Results</p>
    <a href="#" class="btn-blue">100% Money Back Guarantee! *</a>
  </div>
</section>

<section>
  <h2 class="abs pitch">The Revolutionary New Solution For Hair Loss That Uses Personalized Medicine To Stop Hair Loss and Regrow Your Thinning / Receding Hair.</h2>
  <div class="abs story">
    <p>Dr. Edwin Quimby, the creator of Halt and reBloom is a renowned hair restoration expert. After seeing first his father and then older brothers thin and go bald, he dedicated his life to finding the cure for hair loss. After initially pioneering the single hair method for hair transplant, he determined there must be a non-surgical solution and spent the last 20 years in research and clinical trial and error first creating, then perfecting what is now the Halt and reBloom solution for hair loss.</p>
    <p>To the right you can see the Quimby family tree, or at least the five Quimby brothers from oldest to youngest. Unluckily for the oldest three Dr Quimby did not discover the cure until it was too late for them. As you can see both Edwin and his younger brother (Edwin is the second youngest) sport a full head of hair despite both now being well beyond the age when their older brothers had already lost their hair.<br>Read more of Dr Quimby story here.</p>
  </div>
  <div class="abs video" role="img" aria-label="Video still of a man running his hand through his hair"></div>
  <div class="abs video-title">Halt and reBloom - See Your Future, Change Your Future</div>
  <div class="abs video-bar"></div>
</section>

<footer>
  <div class="abs footer"></div>
  <div class="abs foot-mark"></div>
  <p class="abs foot-tag">Brightpath Learning is an education platform that partners with top universities and organizations worldwide, to offer courses online for anyone to take.</p>
  <div class="abs foot-rule" style="top:2256px"></div>
  <div class="abs socials"><span></span><span class="on"></span><span></span><span></span><span></span></div>
  <div class="abs col col-about">
    <h3>About Halt &amp; Rebloom</h3>
    <p>Lorem ipsum dolor sit amet, consectet ur adipiscing elit, sed do eiusmod tempor&nbsp; ipsum dolor sit amet, consectet ur adipiscing elit, sed do Lorem ipsum dolor sit amet, consectet ur adipiscing elit, sed do eiusmod tempor incididunt ut labore et eiusmod tempor incididunt ut labore et.</p>
  </div>
  <div class="abs col col-hours">
    <h3>Hours of Operation</h3>
    <p>Monday - Friday: 9.00am to 5.00pm<br>Saturday: 8.00am to 2.00pm<br>Call Us (310) 555-0187<br>&nbsp;(310) 555-0187</p>
  </div>
  <div class="abs col col-address">
    <h3>Addresss</h3>
    <div class="addr">
      <span class="pin"><svg width="12" height="16" viewBox="0 0 12 16" aria-hidden="true"><path d="M6 0a6 6 0 0 0-6 6c0 4 6 10 6 10s6-6 6-10a6 6 0 0 0-6-6z" fill="#fff"/><circle cx="6" cy="6" r="2.3" fill="#1f9fd8"/></svg></span>
      <div>Halt and Rebloom Hair, LLC<br>4120 Larkspur Ave, Suite 300<br>Fairmont CA 90000<br>Email Us</div>
    </div>
  </div>
  <div class="abs foot-rule" style="left:118px;width:964px;top:2584px"></div>
  <p class="abs copyright">© 2016 Copyright Halt &amp; Rebloom . All Right Reserved</p>
</footer>
</body>
</html>
```